Brekko's Motorworks - New and Used Outboard & Snowmobile Parts Banner Ad Design Project

We need a header banner for our existing Storvana store and would like to use this same banner for our ShopNook product listing template. I will also be changing the colors of the Storvana store template per your recommendations to match your banner design.
The banner cannot contain any email, phone number, or contact information. I would like to use my existing piston/gear logo but want the banner to combine both outboard motor and snowmobile into one banner. We are renaming the store from Brekko's Marine to Brekko's Motorworks in order to merge with Tolly's Trail Wreckers (snowmobile parts). I will include the logo image and our old business cards for reference. Our website is www.brekkomarineparts.example and ShopNook store is https://www.shopnook.example/str/brekkomarineparts.

I will need the following sizes:
1. Banner 1200X270 for shopnook product template and 970 x 432 for website
2. 150X150 and 450 x 200 Tile for shopnook and website with the logo and business name. (I attached an example)

Target Market(s)

people who need parts for their outboard motor and snowmobile

Industry/Entity Type

I sell new and used Outboard Boat Motor Parts and Snowmobile Parts

Requirements
Must have
• The banner will use used in our ShopNook product template and should be 1200X270 and for the website it can be larger and should work with the existing website template layout. I will also need a 150X150 Tile for shopnook with the logo and business name.
Nice to have
• Should represent both outboard and snowmobile related theme. I will change colors of my templates and website design to match new banner.
Should not have
• In the banner, I can't have any contact information per ShopNook rules

```html
<!DOCTYPE html>
<html lang="en">
<head>
<meta charset="utf-8">
<title>Brekko's Motorworks – Banner Set</title>
<link rel="stylesheet" href="https://fonts.googleapis.com/css2?family=Montserrat:wght@600;700&display=swap">
<style>
  :root {
    --page: #ffffff;
    --brand-blue: #1570b8;
    --brand-yellow: #f6c300;
    --deep-brown: #2e1210;
    --white: #ffffff;
    --photo-sky: #d79a48;
    --photo-mid: #9a7552;
    --photo-snow: #4f6778;
    --tile-border: #333333;
    --mark-grey: #a9b0b6;
  }
  * { box-sizing: border-box; margin: 0; padding: 0; }
  html, body { width: 1200px; height: 1200px; overflow: hidden; background: var(--page); }
  body { position: relative; font-family: "Montserrat", Arial, sans-serif; }

  .banner { position: absolute; overflow: hidden; }
  .banner--wide { left: 76px; top: 82px; width: 1050px; height: 236px; }
  .banner--web { left: 176px; top: 440px; width: 850px; height: 378px; }

  .banner__photo {
    position: absolute; inset: 0;
    background: linear-gradient(180deg, var(--photo-sky) 0%, var(--photo-mid) 50%, var(--photo-snow) 100%);
  }
  .banner__panel { position: absolute; inset: 0; width: 100%; height: 100%; }
  .banner__panel polygon { fill: var(--brand-blue); }

  .headline { position: absolute; color: var(--white); font-weight: 700; line-height: 1.12; white-space: nowrap; }
  .headline__amp { color: var(--brand-yellow); font-size: 1.15em; margin-left: 0.2em; }
  .headline__sub { display: block; color: var(--brand-yellow); font-weight: 600; text-align: right; line-height: 1.3; }

  .banner--wide .headline { right: 34px; top: 32px; font-size: 36px; }
  .banner--wide .headline__sub { font-size: 25px; }
  .banner--web .headline { right: 36px; top: 132px; font-size: 36px; }
  .banner--web .headline__sub { font-size: 25px; }

  .brand { position: absolute; display: flex; align-items: center; gap: 12px; }
  .brand__dot { flex: none; border-radius: 50%; background: var(--mark-grey); }
  .brand__name { font-weight: 700; line-height: 1.05; color: var(--white); white-space: nowrap; }

  .banner--wide .brand { left: 44px; top: 58px; }
  .banner--wide .brand__dot { width: 46px; height: 46px; }
  .banner--wide .brand__name { font-size: 30px; }
  .banner--web .brand { left: 38px; top: 132px; }
  .banner--web .brand__dot { width: 56px; height: 56px; }
  .banner--web .brand__name { font-size: 36px; }

  .tile { position: absolute; top: 919px; width: 197px; height: 197px; overflow: hidden; }
  .tile--split { left: 265px; }
  .tile--plain { left: 504px; border: 1px solid var(--tile-border); background: var(--white); }
  .tile--stacked { left: 742px; border: 1px solid var(--tile-border); background: var(--white); }
  .tile__bg { position: absolute; inset: 0; width: 100%; height: 100%; }
  .tile__bg .tile__yellow { fill: var(--brand-yellow); }
  .tile__bg .tile__brown { fill: var(--deep-brown); }

  .tile .brand { left: 0; right: 0; top: 0; bottom: 0; justify-content: center; gap: 8px; }
  .tile .brand__dot { width: 26px; height: 26px; }
  .tile .brand__name { font-size: 17px; }
  .tile--split .brand { left: 30px; top: 16px; }
  .tile--split .brand__name { font-size: 16px; }
  .tile--plain .brand__name, .tile--stacked .brand__name { color: var(--brand-blue); }
  .tile--stacked .brand { flex-direction: column; gap: 10px; text-align: center; }
  .tile--stacked .brand__dot { width: 44px; height: 44px; }
  .tile--stacked .brand__name { font-size: 20px; }
</style>
</head>
<body>

  <section class="banner banner--wide">
    <div class="banner__photo" role="img" aria-label="Photo of a rider on a snowmobile crossing a snowy plain at sunset"></div>
    <svg class="banner__panel" viewBox="0 0 1050 236" preserveAspectRatio="none" aria-hidden="true">
      <polygon points="770,0 1050,0 1050,236 690,236"/>
    </svg>
    <div class="brand">
      <span class="brand__dot" aria-hidden="true"></span>
      <span class="brand__name">Brekko's<br>Motorworks</span>
    </div>
    <h2 class="headline">Outboard<span class="headline__amp">&amp;</span><br>Snowmobile<span class="headline__sub">Motor Parts</span></h2>
  </section>

  <section class="banner banner--web">
    <div class="banner__photo" role="img" aria-label="Photo of a rider on a snowmobile crossing a snowy plain at sunset"></div>
    <svg class="banner__panel" viewBox="0 0 850 378" preserveAspectRatio="none" aria-hidden="true">
      <polygon points="600,0 850,0 850,378 500,378"/>
    </svg>
    <div class="brand">
      <span class="brand__dot" aria-hidden="true"></span>
      <span class="brand__name">Brekko's<br>Motorworks</span>
    </div>
    <h2 class="headline">Outboard<span class="headline__amp">&amp;</span><br>Snowmobile<span class="headline__sub">Motor Parts</span></h2>
  </section>

  <div class="tile tile--split">
    <svg class="tile__bg" viewBox="0 0 197 197" aria-hidden="true">
      <rect class="tile__brown" width="197" height="197"/>
      <polygon class="tile__yellow" points="0,0 121,0 0,180"/>
    </svg>
    <div class="brand">
      <span class="brand__dot" aria-hidden="true"></span>
      <span class="brand__name">Brekko's<br>Motorworks</span>
    </div>
  </div>

  <div class="tile tile--plain">
    <div class="brand">
      <span class="brand__dot" aria-hidden="true"></span>
      <span class="brand__name">Brekko's<br>Motorworks</span>
    </div>
  </div>

  <div class="tile tile--stacked">
    <div class="brand">
      <span class="brand__dot" aria-hidden="true"></span>
      <span class="brand__name">Brekko's<br>Motorworks</span>
    </div>
  </div>

</body>
</html>
```